Holiday Sale 2026 Graphics for New Year

I want to create 10 social media graphics (new Instagram size 4:5 (1080 x 1350 pixels) focusing on our Holiday Sale Graphics, using any of the pics attached. Use the attached pics, NO RANDOM STOCK PHOTOGRAPHY. For the color scheme of the graphics, they should all be complementary to the product colors in the photos.
You can add any of the photos attached but none are required. You can do some of the graphics in all text. I mainly need BOLD text that says one of the headlines with the pics (10 total):
1. 25% OFF Holiday Sale: New You Starts Now!
2. 25% OFF Everything: New Year, New You
3. 25% OFF Christmas Sale 🎁 Feel Amazing Again!
4. Holiday Treat: 25% OFF Your Favorites
5. 25% OFF All Supplements ✨ New Year Reset!
6. Holiday Magic: 25% OFF Every Supplement
7. 25% OFF to Kickstart Your New Year Goals
8. New Year, New Waistline! 25% OFF Sale
9. Holiday Sale: 25% OFF Everything
10. A Better You Begins With 25% OFF

```html
<!DOCTYPE html>
<html lang="en">
<head>
<meta charset="utf-8">
<title>Holiday Sale Graphics</title>
<link rel="stylesheet" href="https://fonts.googleapis.com/css2?family=Oswald:wght@500;700&family=Montserrat:wght@400;800;900&family=Archivo+Black&family=Great+Vibes&family=Libre+Baskerville:ital@1&display=swap">
<style>
:root{
  --stage:#a6a6a6;
  --plum:#9b3a6e;
  --pink:#b65a92;
  --ink:#1f1f1f;
  --red:#e01b1b;
  --brown:#5b2f1f;
  --marble:#e9e6e2;
  --forest:#1f3a2e;
  --teal:#1d6b50;
  --royal:#2256c6;
  --navy:#2b2a5c;
  --rose:#d11c1c;
  --lime:#6aaa2e;
  --white:#ffffff;
}
*{margin:0;padding:0;box-sizing:border-box}
html,body{width:1200px;height:3484px;overflow:hidden;background:var(--stage)}
.canvas{position:relative;width:1200px;height:3484px;background:var(--stage)}
.panel{position:absolute;width:494px;height:617px;overflow:hidden}
.col-left{left:77px}.col-right{left:620px}
.row-1{top:107px}.row-2{top:766px}.row-3{top:1425px}.row-4{top:2084px}.row-5{top:2743px}
.t{position:absolute;line-height:1;white-space:nowrap}
.cond{font-family:'Oswald',sans-serif;font-weight:700}
.wide{font-family:'Archivo Black',sans-serif}
.geo{font-family:'Montserrat',sans-serif;font-weight:900}
.script{font-family:'Great Vibes',cursive}
.serif-italic{font-family:'Libre Baskerville',serif;font-style:italic}
.center{left:0;right:0;text-align:center}
.photo{position:absolute}

/* 1 */
.sale-card{background:var(--white)}
.sale-card .product-box{position:absolute;left:22px;top:126px;width:451px;height:362px;border-radius:40px;background:#fff;box-shadow:0 4px 18px rgba(0,0,0,.18);overflow:hidden}
.sale-card .product-box .photo{left:0;top:0;width:451px;height:200px;background:linear-gradient(180deg,#f1f1f3,#dcdde2)}

/* 2 */
.resolution-card{background:var(--brown)}
.resolution-card .photo{left:0;top:0;width:300px;height:433px;background:linear-gradient(160deg,#6e3f2b,#2a1a14)}
.resolution-card .counter{position:absolute;left:0;top:433px;width:494px;height:184px;background:var(--marble)}

/* 3 */
.christmas-card{background:radial-gradient(circle at 50% 45%,#ffffff 0%,#ececec 60%,#d9d9d9 100%)}
.christmas-card .tag-outline{position:absolute;left:61px;top:43px;width:362px;height:144px;border:2px solid var(--red);border-radius:6px}
.christmas-card .tag{position:absolute;left:69px;top:35px;width:365px;height:146px;background:var(--red);border-radius:8px 40px 8px 8px}

/* 4 */
.treat-card{background:linear-gradient(180deg,#e0eadb 0%,#c3dfb3 100%)}
.treat-card .rule{position:absolute;left:0;width:494px;height:4px;background:#2a6b4f}

/* 5 */
.reset-card{background:linear-gradient(180deg,#9fb6ea 0%,#e8eefb 45%,#ffffff 70%)}
.reset-card .frame{position:absolute;left:17px;top:98px;width:457px;height:297px;border:2px dotted var(--navy)}
.reset-card .tab{position:absolute;left:42px;top:39px;width:411px;height:171px;background:var(--royal);border-radius:26px 80px 26px 60px}
.reset-card .photo{left:0;top:423px;width:494px;height:194px;background:linear-gradient(180deg,#f4f4f4,#d8d8d8)}

/* 6 */
.magic-card{background:linear-gradient(180deg,#f3b9bd 0%,#fbe6e6 70%)}
.magic-card .photo{left:0;top:118px;width:314px;height:499px;background:linear-gradient(180deg,#f4d3d3,#7a4a3a)}
.magic-card .offer{position:absolute;left:309px;top:253px;width:185px;height:364px;background:#d80d0d;border-radius:90px 0 0 0}

/* 7 */
.goals-card{background:var(--white)}
.goals-card .rule{position:absolute;left:0;width:494px;height:5px;background:#2a6b4f}
.goals-card .photo{left:0;top:352px;width:494px;height:265px;background:linear-gradient(180deg,#ffffff 0%,#5a5a5a 30%,#111 100%)}

/* 8 */
.waistline-card{background:var(--white)}
.waistline-card .band{position:absolute;left:35px;width:249px;background:var(--royal)}

/* 9 */
.magenta-card{background:linear-gradient(180deg,#a04f82,#8a3f70)}

/* 10 */
.better-card{background:linear-gradient(135deg,#3b7637,#5a9a4c)}
.better-card .photo{left:0;top:0;width:246px;height:617px;background:linear-gradient(180deg,#4a6b44,#1b1b1b 55%,#e6e6e6 88%)}
.better-card .badge{position:absolute;left:206px;top:356px;width:256px;height:256px;border-radius:50%;background:var(--lime);box-shadow:0 0 0 10px rgba(140,200,80,.5)}
</style>
</head>
<body>
<main class="canvas">

  <section class="panel sale-card col-left row-1">
    <div class="t cond center" style="top:14px;font-size:103px;color:var(--plum)">25% OFF</div>
    <div class="product-box">
      <div class="photo" role="img" aria-label="Four supplement bottles in a row"></div>
      <div class="t wide center" style="top:204px;font-size:78px;color:var(--ink);text-shadow:4px 4px 0 #c98fb3">HOLIDAY</div>
      <div class="t wide center" style="top:278px;font-size:66px;color:var(--pink)">SALE</div>
    </div>
    <div class="t geo" style="left:51px;top:502px;font-size:48px;font-weight:800;color:var(--ink)">NEW YOU</div>
    <div class="t script" style="left:196px;top:530px;font-size:60px;color:var(--plum)">Starts Now!</div>
  </section>

  <section class="panel resolution-card col-right row-1">
    <div class="photo" role="img" aria-label="Woman smiling behind supplement bottles"></div>
    <div class="counter"></div>
    <div class="t cond" style="right:28px;top:4px;font-size:90px;color:var(--red);letter-spacing:8px">NEW</div>
    <div class="t cond" style="right:26px;top:96px;font-size:98px;color:var(--red)">YEAR</div>
    <div class="t cond" style="right:28px;top:200px;font-size:90px;color:var(--white);letter-spacing:8px">NEW</div>
    <div class="t cond" style="right:32px;top:296px;font-size:104px;color:var(--white)">YOU</div>
    <div class="t wide" style="right:26px;top:440px;font-size:76px;color:var(--red);letter-spacing:2px">25% OFF</div>
    <div class="t cond center" style="top:514px;font-size:84px;color:#111">EVERYTHING</div>
  </section>

  <section class="panel christmas-card col-left row-2">
    <div class="tag-outline"></div>
    <div class="tag"></div>
    <div class="t cond" style="left:69px;width:365px;text-align:center;top:52px;font-size:88px;font-weight:500;color:var(--white)">25% OFF</div>
    <div class="t cond center" style="top:212px;font-size:88px;color:#2a2a2a">CHRISTMAS</div>
    <div class="t cond center" style="top:306px;font-size:88px;color:var(--red)">SALE</div>
    <div class="t cond center" style="top:400px;font-size:78px;font-weight:500;color:#1f1f1f">Feel Amazing</div>
    <div class="t cond center" style="top:492px;font-size:78px;font-weight:500;color:var(--red)">Again!</div>
  </section>

  <section class="panel treat-card col-right row-2">
    <div class="t geo center" style="top:70px;font-size:80px;color:var(--forest)">HOLIDAY</div>
    <div class="t script center" style="top:140px;font-size:130px;color:var(--teal)">Treat</div>
    <div class="rule" style="top:295px"></div>
    <div class="t cond center" style="top:306px;font-size:110px;color:var(--forest)">25% OFF</div>
    <div class="rule" style="top:431px"></div>
    <div class="t geo center" style="top:442px;font-size:68px;font-weight:400;color:var(--forest)">YOUR</div>
    <div class="t geo center" style="top:518px;font-size:66px;color:#1d1d1d">FAVORITES</div>
  </section>

  <section class="panel reset-card col-left row-3">
    <div class="frame"></div>
    <div class="tab"></div>
    <div class="t cond" style="left:42px;width:411px;text-align:center;top:58px;font-size:99px;color:var(--white)">25% OFF</div>
    <div class="t cond center" style="top:222px;font-size:48px;color:var(--navy)">ALL SUPPLEMENTS</div>
    <div class="t wide center" style="top:295px;font-size:60px;color:var(--royal)">NEW YEAR</div>
    <div class="t wide center" style="top:355px;font-size:60px;color:var(--navy)">RESET!</div>
    <div class="photo" role="img" aria-label="Four supplement bottles in a row"></div>
  </section>

  <section class="panel magic-card col-right row-3">
    <svg class="photo" style="left:-60px;top:-60px" width="170" height="170" viewBox="0 0 170 170" aria-hidden="true">
      <g fill="none" stroke="#d11c1c" stroke-width="2"><circle cx="85" cy="85" r="20"/><circle cx="85" cy="85" r="38"/><circle cx="85" cy="85" r="56"/><circle cx="85" cy="85" r="74"/></g>
    </svg>
    <div class="photo" role="img" aria-label="Woman smiling behind a row of supplement bottles"></div>
    <div class="offer"></div>
    <svg class="photo" style="left:400px;top:540px" width="160" height="160" viewBox="0 0 160 160" aria-hidden="true">
      <g fill="none" stroke="#ffffff" stroke-width="2"><circle cx="80" cy="80" r="30"/><circle cx="80" cy="80" r="48"/><circle cx="80" cy="80" r="66"/></g>
    </svg>
    <div class="t cond" style="right:14px;top:28px;font-size:90px;color:var(--rose);text-shadow:3px 3px 0 #f2a0a0">HOLIDAY</div>
    <div class="t cond" style="right:48px;top:134px;font-size:92px;color:#1e1e1e;text-shadow:3px 3px 0 #e9a9a9">MAGIC</div>
    <div class="t cond" style="left:309px;width:185px;text-align:center;top:340px;font-size:80px;color:var(--white)">25%</div>
    <div class="t cond" style="left:309px;width:185px;text-align:center;top:446px;font-size:80px;color:var(--white)">OFF</div>
    <div class="t cond" style="left:9px;top:522px;font-size:42px;font-weight:500;color:#1e1e1e">Every Supplement</div>
  </section>

  <section class="panel goals-card col-left row-4">
    <div class="rule" style="top:55px"></div>
    <div class="t cond center" style="top:70px;font-size:110px;color:var(--forest)">25% OFF</div>
    <div class="rule" style="top:197px"></div>
    <div class="t serif-italic center" style="top:214px;font-size:46px;color:#222">to Kickstart Your</div>
    <div class="t cond center" style="top:268px;font-size:66px;font-weight:500;color:var(--teal)">NEW YEAR GOALS</div>
    <div class="photo" role="img" aria-label="Supplement bottles arranged on dark marble"></div>
  </section>

  <section class="panel waistline-card col-right row-4">
    <div class="t cond center" style="top:66px;font-size:92px;font-weight:500;color:var(--royal)">NEW YEAR</div>
    <div class="t geo center" style="top:174px;font-size:72px;color:#111">NEW</div>
    <div class="t geo center" style="top:262px;font-size:66px;color:#111">WAISTLINE!</div>
    <div class="t cond center" style="top:364px;font-size:116px;font-weight:500;color:var(--royal)">25% OFF</div>
    <div class="band" style="top:550px;height:6px"></div>
    <div class="band" style="top:562px;height:14px"></div>
    <div class="t script" style="left:292px;top:488px;font-size:96px;color:var(--navy)">Sale</div>
  </section>

  <section class="panel magenta-card col-left row-5">
    <svg class="photo" style="left:0;top:0" width="494" height="617" viewBox="0 0 494 617" aria-hidden="true">
      <polygon points="0,146 355,329 0,559" fill="#d65aa6"/>
      <polygon points="0,200 300,329 0,520" fill="#c24b93" opacity=".5"/>
    </svg>
    <div class="t geo" style="left:26px;top:34px;font-size:86px;color:var(--white)">HOLIDAY</div>
    <div class="t script" style="left:218px;top:118px;font-size:128px;color:var(--white)">Sale</div>
    <div class="t cond" style="left:22px;top:256px;font-size:110px;font-weight:500;color:var(--white)">25%</div>
    <div class="t cond" style="left:22px;top:376px;font-size:110px;font-weight:500;color:var(--white)">OFF</div>
    <div class="t geo" style="left:26px;top:516px;font-size:64px;font-weight:800;color:var(--white)">EVERYTHING</div>
  </section>

  <section class="panel better-card col-right row-5">
    <div class="photo" role="img" aria-label="Woman smiling behind supplement bottles"></div>
    <div class="t geo" style="right:40px;top:42px;font-size:44px;color:var(--white)">A BETTER</div>
    <div class="t geo" style="right:44px;top:92px;font-size:102px;color:var(--white)">YOU</div>
    <div class="t geo" style="right:40px;top:198px;font-size:56px;color:var(--white)">BEGINS</div>
    <div class="t geo" style="right:40px;top:256px;font-size:88px;color:var(--white)">WITH</div>
    <div class="badge"></div>
    <div class="t cond" style="left:206px;width:256px;text-align:center;top:404px;font-size:96px;font-weight:500;color:var(--white)">25%</div>
    <div class="t cond" style="left:206px;width:256px;text-align:center;top:500px;font-size:88px;font-weight:500;color:var(--white)">OFF</div>
  </section>

</main>
</body>
</html>
```